Esthetically Pleasing Core Values and Brand Promise for Accounting Firm

I would like a cohesive design that ties together my core values and brand promise. My firm, Maple Finch Advisory, provides accounting work to small businesses. I prefer modern and clean designs. I want my Core Values and Brand Promise to represent me - sole entrepreneur, married, mother of two kids, modern esthetics, clean lines, organized, colorful (teals, greys, white, yellows)

Industry/Entity Type

Public Accounting

Colors
33b8a4

```html
<!DOCTYPE html>
<html lang="en">
<head>
<meta charset="utf-8">
<title>Maple Finch Advisory — Core Values &amp; Brand Promise</title>
<link href="https://fonts.googleapis.com/css2?family=Poppins:wght@700&family=Roboto:wght@400&display=swap" rel="stylesheet">
<style>
  :root {
    --backdrop: #e4e4e5;
    --paper: #f0f0f1;
    --frame-line: #6a6a6a;
    --ink: #555758;
    --teal-1: #b0d8cf;
    --teal-2: #90c8bd;
    --teal-3: #68baab;
    --teal-4: #1f9a94;
    --teal-band: #1f9a95;
    --yellow-1: #efdc6b;
    --yellow-2: #f1e18a;
    --yellow-3: #f1e3a2;
    --footer-yellow: #efe08a;
    --white: #ffffff;
  }
  * { box-sizing: border-box; margin: 0; padding: 0; }
  html, body {
    width: 1135px; height: 1200px; overflow: hidden;
    background: var(--backdrop);
    font-family: "Roboto", Arial, sans-serif;
  }
  .sheet {
    position: absolute; left: 167px; top: 30px;
    width: 800px; height: 1140px;
    background: var(--paper);
  }
  .frame {
    position: absolute; left: 23px; top: 21px;
    width: 751px; height: 944px;
    border: 1.5px solid var(--frame-line);
    overflow: hidden;
  }
  .promise-band { position: absolute; left: 0; top: 0; width: 751px; height: 944px; }
  .group-label {
    position: absolute; width: 200px; margin-left: -100px;
    text-align: center;
    font-family: "Poppins", Arial, sans-serif; font-weight: 700;
    font-size: 28px; line-height: 32px;
  }
  .group-label--values { left: 122px; top: 198px; color: var(--ink); }
  .group-label--promise { left: 122px; top: 690px; color: var(--white); }
  .bracket {
    position: absolute; left: 211px; width: 25px;
    border: 1.5px solid var(--ink); border-right: none;
  }
  .bracket--values { top: 91px; height: 319px; }
  .bracket--promise { top: 626px; height: 212px; border-color: var(--white); }
  .dot {
    position: absolute; left: 251px; width: 98px; height: 98px;
    margin-top: -49px; border-radius: 50%;
  }
  .value { position: absolute; left: 368px; width: 330px; color: var(--ink); }
  .value__title { font-size: 26px; line-height: 30px; margin-bottom: 4px; }
  .value__text { font-size: 14.5px; line-height: 18px; }
  .promise {
    position: absolute; left: 368px; margin-top: -17px;
    font-size: 26px; line-height: 34px; color: var(--white);
  }
  .footer {
    position: absolute; left: 0; top: 988px; width: 800px; height: 152px;
    background: var(--footer-yellow); color: var(--ink);
  }
  .footer__note { position: absolute; width: 232px; font-size: 11.5px; line-height: 14.5px; }
  .footer__note--accounting { left: 66px; top: 43px; width: 205px; }
  .footer__note--tax { left: 328px; top: 39px; }
  .brand-name {
    position: absolute; left: 600px; top: 46px; width: 150px;
    text-align: center; color: var(--teal-4);
    font-size: 21px; line-height: 25px;
  }
</style>
</head>
<body>
<main class="sheet">
  <section class="frame">
    <svg class="promise-band" viewBox="0 0 751 944" aria-hidden="true">
      <path d="M0 569 C160 490 460 470 751 659 L751 944 L0 944 Z" fill="var(--teal-band)"/>
    </svg>

    <h2 class="group-label group-label--values">core<br>values</h2>
    <div class="bracket bracket--values"></div>

    <div class="dot" style="top:91px;background:var(--teal-1)"></div>
    <div class="dot" style="top:197px;background:var(--teal-2)"></div>
    <div class="dot" style="top:304px;background:var(--teal-3)"></div>
    <div class="dot" style="top:410px;background:var(--teal-4)"></div>

    <div class="value" style="top:55px">
      <h3 class="value__title">empower</h3>
      <p class="value__text">we are dedicated, appreciative and respectful of people’s time and purpose.</p>
    </div>
    <div class="value" style="top:160px">
      <h3 class="value__title">client focused</h3>
      <p class="value__text">we provide a personal service that goes above the standards of professional care.</p>
    </div>
    <div class="value" style="top:267px">
      <h3 class="value__title">rectitude</h3>
      <p class="value__text">we know the difference between what we have the right to do and what the right thing to do is.</p>
    </div>
    <div class="value" style="top:378px">
      <h3 class="value__title">relentless</h3>
      <p class="value__text">We believe that the longer we try to do our best, the better we become.</p>
    </div>

    <h2 class="group-label group-label--promise">brand<br>promise</h2>
    <div class="bracket bracket--promise"></div>

    <div class="dot" style="top:626px;background:var(--yellow-1)"></div>
    <div class="dot" style="top:731px;background:var(--yellow-2)"></div>
    <div class="dot" style="top:838px;background:var(--yellow-3)"></div>

    <p class="promise" style="top:626px">trust</p>
    <p class="promise" style="top:726px">dependability</p>
    <p class="promise" style="top:840px">transparency</p>
  </section>

  <footer class="footer">
    <p class="footer__note footer__note--accounting">Accounting - Maple Finch provides all business owners with the financial visibility needed to foster growth and facilitate goals.</p>
    <p class="footer__note footer__note--tax">Tax - Maple Finch provides all clients with a trusted tax advisor who provides accuracy in all filings and ensures your compliance with all government agencies.</p>
    <p class="brand-name">Maple Finch Advisory</p>
  </footer>
</main>
</body>
</html>
```